Healthcare marketing Website design

This is for a healthcare marketing agency
All details and brief included in the files

I need the design to be incredible!

5 pages to be designed
Home page
About
Portfolio Page
Services
Start your project page

If you need more stock images - download preview images from kelmora pix so I can purchase at a later date

```html
<!DOCTYPE html>
<html lang="en">
<head>
<meta charset="utf-8">
<title>Lumen Axis Consulting – Healthcare Marketing</title>
<link rel="stylesheet" href="https://fonts.googleapis.com/css2?family=Josefin+Sans:wght@300;400;600;700&family=Montserrat:wght@400;500;600;700&display=swap">
<style>
:root{
  --navy:#1f3466;
  --navy-deep:#1a2542;
  --blue:#2c4c8c;
  --cyan:#1aa3e4;
  --text:#3d4350;
  --muted:#6b7280;
  --line:#dde3ea;
  --light:#f6f8fa;
  --white:#ffffff;
}
*{box-sizing:border-box;margin:0;padding:0}
html,body{width:1200px;height:4505px;overflow:hidden}
body{position:relative;background:var(--white);font-family:"Montserrat",sans-serif;color:var(--text)}
.abs{position:absolute}
.brand{font-family:"Montserrat",sans-serif;font-weight:500;color:var(--cyan);display:flex;align-items:center;gap:10px;white-space:nowrap}
.brand .dot{width:34px;height:34px;border-radius:50%;background:var(--cyan);flex:none}
.heading{font-family:"Josefin Sans",sans-serif;font-weight:400;color:var(--navy);letter-spacing:-.5px;text-transform:uppercase}
.heading .accent{color:var(--cyan)}
.btn{position:absolute;display:flex;align-items:center;justify-content:center;border-radius:22px;font-size:11px;font-weight:700;letter-spacing:.3px;text-transform:uppercase;height:40px}
.btn-fill{background:var(--cyan);color:var(--white)}
.btn-line{border:1.5px solid var(--cyan);color:var(--cyan);background:transparent}
.btn-ghost{border:1.5px solid var(--white);color:var(--white)}

/* hero */
.hero{position:absolute;left:0;top:0;width:1200px;height:686px;background:linear-gradient(180deg,#3c5c9c 0%,#2f4f8f 60%,#2a4884 100%)}
.hero-photo{position:absolute;inset:0;background:radial-gradient(ellipse at 60% 35%,rgba(150,175,215,.35),rgba(40,70,130,0) 60%)}
.nav{position:absolute;top:78px;left:595px;display:flex;gap:54px;color:var(--white);font-size:12px;font-weight:500;text-transform:uppercase}
.hero h1{position:absolute;top:298px;left:0;width:1200px;text-align:center;font-family:"Josefin Sans",sans-serif;font-weight:400;font-size:44px;line-height:52px;color:var(--white)}
.hero .sub{position:absolute;left:0;width:1200px;text-align:center;color:var(--white);font-family:"Josefin Sans",sans-serif}
.social{display:flex;gap:14px}
.social span{width:10px;height:10px;border-radius:50%;border:1.5px solid currentColor;display:block}

.stats{position:absolute;top:596px;left:98px;display:flex;gap:26px}
.stat{width:231px;height:240px;background:var(--white);box-shadow:0 8px 24px rgba(20,40,80,.12);padding:44px 0 0 44px;position:relative}
.stat b{display:block;font-family:"Josefin Sans",sans-serif;font-size:44px;font-weight:400;color:var(--navy)}
.stat i{display:block;width:38px;height:1.5px;background:var(--cyan);margin:22px 0 24px}
.stat p{font-size:12px;line-height:19px;color:var(--muted);width:150px}
.stat::after{content:"";position:absolute;left:34px;right:34px;bottom:0;height:3px;background:var(--cyan)}

/* about */
.about-title{top:918px;left:98px;font-size:34px;display:flex;align-items:flex-end;gap:12px}
.about-title .brand{font-size:30px}
.lead{font-weight:600;font-size:14px;color:var(--navy)}
.copy{font-size:12.5px;line-height:27px;color:var(--text)}
.about-img{top:922px;left:673px;width:429px;height:283px;background:linear-gradient(135deg,#e9f3fb,#9cc9ec 55%,#4d8fd0)}
.about-block{top:1105px;left:1102px;width:98px;height:238px;background:var(--blue)}
.about-box{top:1205px;left:749px;width:451px;height:138px;background:var(--blue);color:var(--white);font-size:14px;line-height:25px;padding:28px 20px 0 45px}
.about-badge{top:1237px;left:703px;width:70px;height:70px;border-radius:50%;background:var(--white);box-shadow:0 4px 14px rgba(0,0,0,.15)}

/* since */
.since{position:absolute;top:1431px;left:0;width:1200px;height:496px;background:linear-gradient(90deg,#c9dde6 0%,#dfecef 45%,#e3f0f1 100%)}
.since-img{position:absolute;left:0;top:0;width:600px;height:496px;background:linear-gradient(90deg,#0f3c63 0%,#3f7ea4 45%,rgba(210,228,234,0) 100%)}

/* strip */
.strip{top:2015px;left:196px;width:806px;height:110px;border-top:1px solid var(--line);border-bottom:1px solid var(--line)}
.strip-item{position:absolute;top:16px;width:170px;text-align:center;font-size:11.5px;font-weight:700;color:var(--navy);line-height:16px}
.strip-item svg{display:block;margin:0 auto 8px}

/* reviews */
.reviews{position:absolute;top:2293px;left:0;width:1200px;height:540px;background:linear-gradient(160deg,#1d4f96 0%,#1b5ea8 50%,#174a8e 100%)}
.review{position:absolute;top:156px;width:451px;height:178px;border:1px solid rgba(255,255,255,.35);background:rgba(20,50,110,.45);padding:20px 24px 0 24px;color:var(--white)}
.review h4{font-size:13.5px;font-weight:700;display:flex;gap:14px;align-items:center}
.review p{font-size:12px;line-height:24px;margin-top:6px}
.avatar{position:absolute;width:70px;height:70px;border-radius:50%;border:3px solid var(--white);background:linear-gradient(180deg,#d9c7b8,#8f7a6a)}
.reviewer{position:absolute;font-size:13.5px;font-weight:700;color:var(--white)}

/* faq */
.faq{position:absolute;top:2833px;left:0;width:1200px;height:586px;background:var(--light)}
.faq-item{position:absolute;left:219px;width:778px;border-bottom:1px solid var(--line);font-size:15px;font-weight:500;color:var(--navy-deep)}
.faq-icon{position:absolute;right:0;width:18px;height:18px;border-radius:50%;background:var(--navy-deep)}
.faq-icon::before,.faq-icon::after{content:"";position:absolute;background:var(--white);left:4px;top:8px;width:10px;height:2px}
.faq-icon.plus::after{left:8px;top:4px;width:2px;height:10px}
.faq-icon.open{background:var(--cyan)}

/* blogs */
.blog{position:absolute;top:3577px;width:315px;height:385px;background:var(--white);box-shadow:0 8px 24px rgba(20,40,80,.1)}
.blog-img{height:201px;position:relative}
.blog-date{position:absolute;left:22px;bottom:-8px;background:var(--navy-deep);color:var(--white);font-size:10px;font-weight:600;padding:4px 8px}
.blog h3{font-family:"Josefin Sans",sans-serif;font-size:15px;font-weight:600;line-height:28px;color:var(--navy-deep);margin:20px 22px 0}
.blog p{font-size:11.5px;line-height:19px;color:var(--muted);margin:12px 22px 0}
.blog .more{position:absolute;left:22px;bottom:26px;font-size:10px;font-weight:700;color:var(--cyan);display:flex;gap:8px;align-items:center}

/* footer */
.footer{position:absolute;top:4131px;left:0;width:1200px;height:374px;background:var(--navy-deep);color:var(--white)}
.footer .col-title{position:absolute;font-family:"Josefin Sans",sans-serif;font-size:15px;text-transform:uppercase}
.footer .links{position:absolute;left:509px;top:98px;font-size:12px;line-height:30px;text-transform:uppercase;color:#c9d1e3}
.footer .info{position:absolute;left:149px;font-size:11.5px;line-height:17px}
.footer small{color:#aab3c8;font-size:11px}
</style>
</head>
<body>

<!-- hero -->
<section class="hero">
  <div class="hero-photo" role="img" aria-label="Photo of a smiling doctor in a clinic, tinted blue"></div>
  <div class="brand abs" style="top:40px;left:98px;font-size:34px;color:var(--white)"><span class="dot"></span><span>lumen axis <small style="font-size:12px;vertical-align:bottom;letter-spacing:.5px">CONSULTING</small></span></div>
  <div class="social abs" style="top:33px;left:888px;color:var(--white)"><span aria-label="Social link"></span><span aria-label="Social link"></span></div>
  <div class="btn abs" style="top:19px;left:948px;width:152px;height:38px;background:var(--white);color:var(--cyan)">Contact Us</div>
  <nav class="nav"><span>Home</span><span>About</span><span>Our Services</span><span>Portfolio</span><span>Blog</span></nav>
  <h1>DON’T MISS A NEW OPPORTUNITY<br>TO GROW YOU PRACTICE</h1>
  <div class="sub" style="top:414px;font-size:17px;font-weight:300">WITH YOUR ONLINE PRESENCE</div>
  <div class="sub" style="top:459px;font-size:15px"><span style="color:var(--cyan)">BEING ONLINE</span>: A LARGE OPPORTUNITY FOR YOUR PRACTICE</div>
  <div class="btn btn-ghost" style="top:503px;left:505px;width:190px">Start Your Project</div>
</section>

<div class="stats">
  <div class="stat"><b>80%</b><i></i><p>Of internet uses search for health information</p></div>
  <div class="stat"><b>50%</b><i></i><p>Would like information about a specific health professional</p></div>
  <div class="stat"><b>42%</b><i></i><p>Of individuals look at health related consumer reviews</p></div>
  <div class="stat"><b>41%</b><i></i><p>Of consumers say online presence may impact their choice of health professional</p></div>
</div>

<!-- about -->
<h2 class="heading abs about-title">About <span class="brand" style="font-size:30px">lumen axis</span></h2>
<div class="lead abs" style="top:995px;left:100px">Helping Those Who Help Others</div>
<p class="copy abs" style="top:1028px;left:100px;width:520px">You became a health professional because you wanted to make a difference and you obviously care about patient outcomes. At first things were great and you had plenty of patients but in the last few years there’s more competition offering the same types of services and products that you do. Regular customers haven’t come back to you in a while and you know you NEED to do something but the old ways like relying on word of mouth doesn’t seem to be working well anymore and you don’t know how to get started.</p>
<p class="copy abs" style="top:1230px;left:100px;width:520px">But that’s where we can help... Lumen Axis Consulting specialises in helping health professionals like you to create a great online user experience for your patients.</p>
<div class="btn btn-fill" style="top:1305px;left:98px;width:150px">Contact Us</div>
<div class="btn btn-line" style="top:1305px;left:266px;width:196px">Start Your Project</div>
<div class="abs about-block"></div>
<div class="abs about-img" role="img" aria-label="Illustration of a laptop with medical charts and a stethoscope"></div>
<div class="abs about-box">We help you build your online assets through Website development, social media marketing, Online Traffic Strategies.</div>
<div class="abs about-badge"></div>

<!-- since -->
<section class="since">
  <div class="since-img" role="img" aria-label="Doctor touching a digital human body and molecule graphics"></div>
  <h2 class="heading abs" style="top:100px;left:598px;font-size:34px">Helping <span class="accent">Clients since 2015</span></h2>
  <div class="lead abs" style="top:160px;left:600px">Lumen Axis Consulting</div>
  <p class="copy abs" style="top:196px;left:600px;width:500px">Specialises in helping health professionals like you, stand out from the busy crowd, find new patient and helps you be seen as the go-to person within your industry. Unlike most health professionals who solely rely on word of mouth, we use the latest online marketing techniques to grow you and your practice.</p>
  <p class="copy abs" style="top:322px;left:600px;width:500px">While our niche has always been in the healthcare industry, Lumen Axis Marketing also has experience in providing solutions our e-commerce partners as well as other professional industries.</p>
</section>

<!-- strip -->
<div class="abs strip">
  <div class="brand abs" style="top:34px;left:26px;font-size:33px"><span class="dot"></span>lumen axis</div>
  <div class="abs" style="top:24px;left:276px;width:1px;height:62px;background:var(--line)"></div>
  <div class="strip-item" style="left:305px"><svg width="40" height="34" viewBox="0 0 40 34" fill="none" stroke="#1aa3e4" stroke-width="2"><path d="M20 31 C4 20 2 12 6 6 C10 1 17 2 20 8 C23 2 30 1 34 6 C38 12 36 20 20 31Z"/><path d="M6 16 H14 L17 10 L22 22 L25 16 H34"/></svg>63% HEALTHCARE<br>AND MEDICAL</div>
  <div class="strip-item" style="left:455px"><svg width="40" height="34" viewBox="0 0 40 34" fill="none" stroke="#1aa3e4" stroke-width="2"><rect x="8" y="3" width="24" height="26" rx="2"/><path d="M12 10 H28 M12 16 H28 M12 22 H22"/></svg>25% ECOMMERCE<br>PROJECTS</div>
  <div class="strip-item" style="left:625px"><svg width="40" height="34" viewBox="0 0 40 34" fill="none" stroke="#1aa3e4" stroke-width="2"><rect x="6" y="4" width="28" height="20" rx="2"/><path d="M14 30 H26 M20 24 V30 M12 18 L18 12 L22 16 L28 10"/></svg>12% OTHER<br>PROFESSIONAL SERVICES</div>
</div>
<div class="btn btn-fill" style="top:2166px;left:418px;width:152px">Contact Us</div>
<div class="btn btn-line" style="top:2166px;left:586px;width:196px">Start Your Project</div>

<!-- reviews -->
<section class="reviews" role="img" aria-label="Blue medical technology background">
  <h2 class="heading abs" style="top:82px;left:0;width:1200px;text-align:center;font-size:34px;color:var(--white)">Customer <span class="accent">Reviews</span></h2>
  <div class="review" style="left:119px"><h4><span style="color:var(--cyan);font-size:38px;line-height:20px">“</span>Dignissim qui blandit praesent augue duis.</h4><p>Lorem ipsum dolor sit amet, consectetuer adipiscing elit, diam nonummy nibh euismod tincidunt ut laoreet dolore magna aliquam erat volutpat. Ut wisi enim ad minim veniam.</p></div>
  <div class="review" style="left:633px"><h4><span style="color:var(--cyan);font-size:38px;line-height:20px">“</span>Dignissim qui blandit praesent augue duis.</h4><p>Lorem ipsum dolor sit amet, consectetuer adipiscing elit, diam nonummy nibh euismod tincidunt ut laoreet dolore magna aliquam erat volutpat. Ut wisi enim ad minim veniam.</p></div>
  <div class="avatar" style="top:290px;left:150px" role="img" aria-label="Portrait of reviewer"></div>
  <div class="reviewer" style="top:304px;left:240px">Mara Linden</div>
  <div class="avatar" style="top:290px;left:664px" role="img" aria-label="Portrait of reviewer"></div>
  <div class="reviewer" style="top:304px;left:754px">Tessa Quill</div>
  <div class="abs" style="top:372px;left:575px;display:flex;gap:12px"><span style="width:10px;height:10px;border-radius:50%;background:#fff"></span><span style="width:10px;height:10px;border-radius:50%;background:rgba(255,255,255,.45)"></span><span style="width:10px;height:10px;border-radius:50%;background:rgba(255,255,255,.45)"></span></div>
  <div class="btn" style="top:415px;left:418px;width:152px;background:var(--white);color:var(--cyan)">Contact Us</div>
  <div class="btn btn-ghost" style="top:415px;left:586px;width:196px">Start Your Project</div>
</section>

<!-- faq -->
<section class="faq">
  <h2 class="heading abs" style="top:82px;left:0;width:1200px;text-align:center;font-size:34px">Frequently <span class="accent">Asked Question</span></h2>
</section>
<div class="faq-item" style="top:2990px;height:124px">Lorem Ipsum Dolor Sit Amet, Consectetur Adipiscing Elit?<span class="faq-icon open" style="top:2px"></span>
  <p style="font-size:13px;font-weight:400;line-height:26px;color:var(--text);margin-top:10px;width:720px">Duis aute irure dolor in reprehenderit in voluptate velit esse cillum dolore eu fugiat nulla pariatur. Excepteur sint occaecat cupidatat non proident, sunt in culpa qui officia deserunt mollit anim id est laborum non proident, sunt in culpa qui officia.</p></div>
<div class="faq-item" style="top:3133px;height:60px">Sed Ut Perspiciatis Unde Omnis Iste Natus Error Sit Voluptatem Accusantium?<span class="faq-icon plus" style="top:2px"></span></div>
<div class="faq-item" style="top:3193px;height:60px">Nemo Enim Ipsam Voluptatem Quia Voluptas Sit Aspernatur Aut Odit Aut Fugit?<span class="faq-icon plus" style="top:2px"></span></div>
<div class="faq-item" style="top:3253px;height:60px">Quia Voluptas Sit Aspernatur Aut Odit Aut Fugit?<span class="faq-icon plus" style="top:2px"></span></div>
<div class="faq-item" style="top:3313px;height:40px;border:none">Ut Enim Ad Minima Veniam, Quis Nostrum Exercitationem?<span class="faq-icon plus" style="top:2px"></span></div>

<!-- blogs -->
<h2 class="heading abs" style="top:3503px;left:0;width:1200px;text-align:center;font-size:34px">Recent <span class="accent">Blogs</span></h2>
<article class="blog" style="left:98px"><div class="blog-img" role="img" aria-label="Hands typing on a laptop keyboard" style="background:linear-gradient(135deg,#5b7fa6,#c9d8e6 60%,#e9c79a)"><span class="blog-date">Jan 30, 2022</span></div><h3>Lorem Ipsum Dolor Sit Amet, Conse Ctetuer Adipiscing Elit?</h3><p>Excepteur sint occaecat cupidatat non proident, sunt in culpa qui officia..</p><span class="more">READ MORE <svg width="14" height="8" viewBox="0 0 14 8" fill="none" stroke="#1aa3e4" stroke-width="1.5"><path d="M0 4 H12 M9 1 L12 4 L9 7"/></svg></span></article>
<article class="blog" style="left:443px"><div class="blog-img" role="img" aria-label="Designers sketching website wireframes" style="background:linear-gradient(135deg,#2f5878,#9ab8cc 55%,#e2e8ee)"><span class="blog-date">Mar 29, 2022</span></div><h3>Lorem Ipsum Dolor Sit Amet, Conse Ctetuer Adipiscing Elit?</h3><p>Excepteur sint occaecat cupidatat non proident, sunt in culpa qui officia..</p><span class="more">READ MORE <svg width="14" height="8" viewBox="0 0 14 8" fill="none" stroke="#1aa3e4" stroke-width="1.5"><path d="M0 4 H12 M9 1 L12 4 L9 7"/></svg></span></article>
<article class="blog" style="left:787px"><div class="blog-img" role="img" aria-label="Hand using laptop with rating icons" style="background:linear-gradient(135deg,#8a96a6,#cfd6de 55%,#eef1f4)"><span class="blog-date">Mar 07, 2022</span></div><h3>Lorem Ipsum Dolor Sit Amet, Conse Ctetuer Adipiscing Elit?</h3><p>Excepteur sint occaecat cupidatat non proident, sunt in culpa qui officia..</p><span class="more">READ MORE <svg width="14" height="8" viewBox="0 0 14 8" fill="none" stroke="#1aa3e4" stroke-width="1.5"><path d="M0 4 H12 M9 1 L12 4 L9 7"/></svg></span></article>
<div class="btn btn-fill" style="top:4006px;left:525px;width:150px">More Blogs</div>

<!-- footer -->
<footer class="footer">
  <div class="brand abs" style="top:56px;left:149px;font-size:34px"><span class="dot"></span><span>lumen axis <small style="font-size:11px;color:var(--white)">CONSULTING</small></span></div>
  <svg class="abs" style="top:136px;left:146px" width="14" height="18" viewBox="0 0 14 18" fill="none" stroke="#1aa3e4" stroke-width="1.6"><path d="M7 17 C2 11 1 8 1 6 A6 6 0 0 1 13 6 C13 8 12 11 7 17Z"/><circle cx="7" cy="6" r="2"/></svg>
  <div class="info" style="top:136px;left:174px"><b>Lorem Ipsum Dolor</b><br><small>1234 consectetur adipis<br>cingelit, sed do</small></div>
  <svg class="abs" style="top:218px;left:146px" width="16" height="16" viewBox="0 0 16 16" fill="none" stroke="#1aa3e4" stroke-width="1.6"><path d="M3 1 L6 1 L7 5 L5 6 C6 8 8 10 10 11 L11 9 L15 10 L15 13 C15 14 14 15 13 15 C6 15 1 10 1 3 C1 2 2 1 3 1Z"/></svg>
  <div class="info" style="top:216px;left:174px"><small>Toll Free:</small> <b>555.014.220</b><br><small>Fax:</small> <b>555.014.221</b></div>
  <svg class="abs" style="top:266px;left:146px" width="16" height="12" viewBox="0 0 16 12" fill="none" stroke="#1aa3e4" stroke-width="1.5"><rect x="1" y="1" width="14" height="10"/><path d="M1 1 L8 7 L15 1"/></svg>
  <div class="info" style="top:264px;left:174px"><b>hello@lumenaxis.example</b></div>
  <div class="col-title" style="top:60px;left:509px">Links</div>
  <div class="links">Home<br>About<br>Our Services<br>Portfolio<br>Blog<br>Contact Us</div>
  <div class="col-title" style="top:56px;left:743px">Signup for our newsletter</div>
  <div class="abs" style="top:100px;left:743px;width:247px;height:40px;border:1px solid #3c4868;border-radius:20px;font-size:12px;color:#aab3c8;padding:12px 20px">Email Address *</div>
  <div class="btn btn-fill" style="top:158px;left:743px;width:151px;height:38px">Submit</div>
  <small class="abs" style="top:337px;left:147px">©2022 Lumen Axis Consulting</small>
  <div class="social abs" style="top:339px;left:518px;color:var(--cyan)"><span aria-label="Social link"></span><span aria-label="Social link"></span></div>
  <small class="abs" style="top:337px;left:766px">Privacy Policy &nbsp;|&nbsp; Terms And Conditions</small>
</footer>

</body>
</html>
```